Book Cover " FROM GRAVEL TO AMBER"

Looking for a book cover for a novel from Gravel to Amber.
Amber is the characters developed name. The book describes his rough up bringing and how he obtains his greatness and his given name Amber.

```html
<!DOCTYPE html>
<html lang="en">
<head>
<meta charset="utf-8">
<title>From Gravel to Amber – Book Cover</title>
<link rel="stylesheet" href="https://fonts.googleapis.com/css2?family=Barlow+Condensed:wght@700;800&family=Kaushan+Script&display=swap">
<style>
  :root {
    --page-bg: #e8e8e8;
    --silk-deep: #141c4a;
    --silk-mid: #27369a;
    --silk-light: #4c66c8;
    --silk-haze: #7b8ac4;
    --title-white: #ffffff;
    --title-peach: #f3c2ad;
    --cover-shadow: rgba(0, 0, 0, 0.28);
  }
  * { margin: 0; padding: 0; box-sizing: border-box; }
  html, body {
    width: 1200px;
    height: 800px;
    overflow: hidden;
    background: var(--page-bg);
  }
  .canvas {
    position: relative;
    width: 1200px;
    height: 800px;
    display: flex;
    align-items: center;
    justify-content: center;
  }
  .book-cover {
    position: relative;
    width: 500px;
    height: 730px;
    overflow: hidden;
    box-shadow: 0 14px 40px var(--cover-shadow);
  }
  .cover-art {
    position: absolute;
    inset: 0;
    background:
      radial-gradient(ellipse 60% 30% at 70% 20%, var(--silk-light) 0%, transparent 70%),
      radial-gradient(ellipse 50% 25% at 25% 60%, var(--silk-haze) 0%, transparent 70%),
      radial-gradient(ellipse 70% 25% at 60% 80%, var(--silk-light) 0%, transparent 75%),
      linear-gradient(160deg, var(--silk-mid) 0%, var(--silk-deep) 45%, var(--silk-mid) 70%, var(--silk-deep) 100%);
  }
  .title {
    position: absolute;
    left: 40px;
    top: 150px;
    right: 30px;
    color: var(--title-white);
  }
  .title-from,
  .title-to {
    display: block;
    font-family: "Barlow Condensed", sans-serif;
    font-weight: 800;
    font-size: 50px;
    line-height: 1;
    letter-spacing: 1px;
    color: var(--title-white);
  }
  .title-from { margin-left: 40px; }
  .title-gravel {
    display: block;
    font-family: "Barlow Condensed", sans-serif;
    font-weight: 700;
    font-size: 130px;
    line-height: 0.9;
    letter-spacing: 2px;
    color: var(--title-peach);
    margin-left: 60px;
  }
  .title-to { margin-top: 6px; }
  .title-amber {
    display: block;
    font-family: "Kaushan Script", cursive;
    font-size: 120px;
    line-height: 1;
    color: var(--title-white);
    margin-left: 10px;
    margin-top: -10px;
  }
</style>
</head>
<body>
  <main class="canvas">
    <section class="book-cover">
      <div class="cover-art" role="img" aria-label="Photograph of rumpled royal blue silk with a faint silhouette of a lone figure on a stone path"></div>
      <h1 class="title">
        <span class="title-from">FROM</span>
        <span class="title-gravel">GRAVEL</span>
        <span class="title-to">TO</span>
        <span class="title-amber">Amber</span>
      </h1>
    </section>
  </main>
</body>
</html>
```